WordPress website in children books redesign

We are personalised children storybook creators with a range of personalized books, music CDs and DVDs that are created for each child. We sell our concept through a license via distributors / entrepreneurs mainly based in France and Europe. We want to focus on selling B2C to parents and grandparents, looking to buy presents to their children aged 0 to 10 years old. Those present are educative, unique for each child, and they will learn to have fun and learn to have fun. I would like to redesign our WordPress website https://pebblelanternkids.co.uk/index.php We are a children in the world of books and music books: books, music CDs and DVDs looking for something a little more along the lines of our competitors. See ike www.quillotop.com, www.tavirosa.com, www.lecheminduvelours.com, https://www.lespetitsbrume.com/, https://tinselpaths.com/ Our current website is a bit too old fashioned so I am looking at a much more modern design Here is a link for a few products that are not available here: https://www.filecrate.example/sh/kq417dzopfrnwtb/BXPL3rYmOk2u-sVH4dQkLN-zb?dl=0 We have 2 sides in our website: B2C on the left side and B2B on the right site; B2B is for distributors that are entrepreneurs buying our concept. for the homepage design, the main focus will be B2Consumer Our current page is too blended, lacks reassurance elements and I would like to have a look at this page. from our current stories. here is a link for our business book to give you a feel for it: http://online.pagewavo.com/qtlk/pzme/ MAIN PAGES TO REVIEW / HOMEPAGE / https://pebblelanternkids.co.uk/ BOOKS: https : //pebblelanternkids.co.uk/product-category/personalised-books/ MUSIC: https://pebblelanternkids.co.uk/product-category/music-cds/ BLOG: https://pebblelanternkids.co.uk/blog -2 / Looking forward to seeing you and your questions asap

Target Market(s)

parents and grandparents of children aged 0 to 10 years old. This is for the European market

Industry/Entity Type

Publishing Company

Number of Pages Required

4 page

Colors
0392cd
9bcb3b
ec1f27
757575

Requirements
Must have
• keep within the color code of our RGB logo: D25028 RGB: 8CC364 329BC8 808285
Nice to have
• be more with the style of our competitors. Pebble Lantern Kids am about making children learn the fun way, and develop their morality, self-esteem and confidence. It's about the magic of reading to help children learn while having fun. I have attached visuals but those are just examples and you we encourage you to suggest other ideas

```html
<!DOCTYPE html>
<html lang="en">
<head>
<meta charset="utf-8">
<title>Pebble Lantern Kids – Home</title>
<link href="https://fonts.googleapis.com/css2?family=Montserrat:wght@600;700&family=Open+Sans:wght@400;600;700&family=Questrial&display=swap" rel="stylesheet">
<style>
:root{
  --blue:#0392cd;
  --navy:#0c2a4a;
  --navy-mid:#124a78;
  --mint:#b7f1cc;
  --green:#3f9a35;
  --green-panel:#6cb43c;
  --green-dark:#2f7f28;
  --grey-bar:#6f6f6f;
  --ink:#333;
  --white:#fff;
}
*{box-sizing:border-box;margin:0;padding:0}
html,body{width:1200px;height:2406px;overflow:hidden}
body{position:relative;font-family:"Open Sans",Arial,sans-serif;color:var(--ink);background:var(--white)}
.abs{position:absolute}
.section-title{font-family:"Questrial",Arial,sans-serif;font-weight:400;color:var(--blue);font-size:22px;letter-spacing:.5px;text-transform:uppercase}
.btn{display:flex;align-items:center;justify-content:center;background:var(--blue);color:var(--white);border-radius:4px;font-size:13px}

/* top bar */
.promo-bar{left:0;top:0;width:1200px;height:22px;background:var(--grey-bar);color:var(--white);font-size:11px;display:flex;align-items:center;justify-content:flex-end;padding-right:256px;gap:8px;z-index:3}
.promo-bar .tag{background:var(--blue);padding:1px 8px;border-radius:8px;font-size:10px}

/* header */
.site-header{left:0;top:22px;width:1200px;height:100px;background:var(--white)}
.brand{left:248px;top:14px;display:flex;align-items:center;gap:8px}
.brand .dot{width:18px;height:18px;border-radius:50%;background:var(--blue)}
.brand .name{font-family:"Open Sans",Arial,sans-serif;font-weight:700;color:var(--blue);font-size:15px}
.main-nav{left:344px;top:48px;display:flex;gap:14px;font-size:10.5px;color:var(--ink);align-items:center;z-index:3}

/* hero */
.hero{left:0;top:122px;width:1200px;height:290px;background:var(--blue)}
.hero-photo{left:752px;top:32px;width:300px;height:370px;background:radial-gradient(ellipse at 50% 40%,#f3d3c4 0%,#e9b9a6 35%,#c98c76 60%,#1f8fc8 88%);border-radius:150px 150px 0 0;z-index:1}
.hero-title{left:249px;top:84px;width:310px;font-family:"Montserrat",Arial,sans-serif;font-weight:700;color:var(--white);font-size:24px;line-height:32px;text-transform:uppercase}
.clouds{left:0;top:350px;width:1200px;height:70px;z-index:2}

/* vision mission */
.intro{left:0;top:412px;width:1200px;height:242px;background:linear-gradient(#eaf7fd,#ffffff)}
.col{position:absolute;font-size:10.5px;line-height:16px;color:var(--ink)}
.col h2{margin-bottom:22px}
.col.vision{left:248px;top:40px;width:262px}
.col.mission{left:541px;top:40px;width:400px}
.divider{left:522px;top:92px;width:1px;height:100px;background:#9fb7c4}

/* products */
.products{left:0;top:654px;width:1200px;height:334px;background:radial-gradient(ellipse at 50% 55%,var(--navy-mid) 0%,var(--navy) 75%)}
.products .section-title{color:var(--white);position:absolute;left:0;width:1200px;text-align:center;top:32px}
.product-card{position:absolute;top:81px;width:219px;height:219px;border:2px solid #49b3e6}
.product-card .btn{position:absolute;left:38px;bottom:14px;width:126px;height:28px;border-radius:5px;font-size:13.5px}

/* about */
.about{left:0;top:988px;width:1200px;height:305px;background:linear-gradient(100deg,#d7eef7 0%,#f5fbfd 30%,#ffffff 60%)}
.about-copy{position:absolute;left:249px;top:62px;width:402px;display:flex;flex-direction:column;align-items:flex-start}
.about-copy p{font-size:10.5px;line-height:16px;margin-top:10px}
.about-copy .btn{width:111px;height:28px;margin-top:14px}
.book-mock{left:706px;top:40px;width:297px;height:240px;background:linear-gradient(135deg,#8fd3b6 0%,#e8f3ee 50%,#cfe6da 100%);transform:skewY(-6deg)}

/* blogs */
.blogs{left:0;top:1293px;width:1200px;height:319px;background:var(--mint)}
.blogs h2{position:absolute;left:0;width:1200px;text-align:center;top:24px}
.arrows{right:254px;top:24px;display:flex;gap:2px}
.blog-card{position:absolute;top:87px;width:204px}
.blog-card .thumb{height:136px;box-shadow:0 4px 6px rgba(0,0,0,.25)}
.blog-card p{font-size:10px;line-height:13px;color:#555;margin-top:20px}

/* video */
.video{left:248px;top:1649px;width:419px;height:229px;background:linear-gradient(135deg,#2a2620,#141210 60%,#3a3020)}
.story{position:absolute;left:692px;top:1672px;width:270px;display:flex;flex-direction:column;align-items:flex-start}
.story h2{font-family:"Questrial",Arial,sans-serif;font-weight:400;font-size:18.5px;line-height:20px;color:var(--blue);text-transform:uppercase}
.story p{font-size:10px;line-height:15px;color:#888;margin-top:8px;width:262px}
.story .btn{width:110px;height:27px;margin-top:12px}

/* garden */
.garden{left:0;top:1880px;width:1200px;height:213px;background:linear-gradient(180deg,#ffffff 0%,#fbe7b8 30%,#9bd26a 70%,#4fa23a 100%)}

/* footer */
.contact{left:0;top:2093px;width:1200px;height:297px;background:var(--green);color:var(--white)}
.contact-info{position:absolute;left:250px;top:26px;width:345px;display:flex;flex-direction:column}
.contact-info h2{font-family:"Questrial",Arial,sans-serif;font-size:25px;font-weight:400}
.contact-info .lead{font-size:10.5px;line-height:16.5px;margin-top:12px}
.contact-line{display:flex;gap:14px;font-size:10.5px;line-height:15px;align-items:flex-start;margin-top:16px}
.contact-line:first-of-type{margin-top:22px}
.form-panel{left:600px;top:27px;width:346px;height:251px;background:var(--green-panel);border-radius:4px}
.field{position:absolute;left:22px;width:302px;border:1px solid #d6edc4;border-radius:3px;font-size:11px;padding:10px 10px}
.submit{position:absolute;left:104px;top:214px;width:130px;height:27px;background:var(--white);color:#333;border-radius:4px;font-size:11px;display:flex;align-items:center;justify-content:center}
.copyright{left:0;top:2390px;width:1200px;height:16px;background:var(--green-dark);color:#fff;font-size:9px;text-align:center;line-height:16px}
</style>
</head>
<body>

<div class="abs promo-bar">Woohoo! 15% de réduction sur tous les livres, CD et DVD (packs et produits distributeurs non inclus) <span class="tag">WOOHOO</span></div>

<header class="abs site-header">
  <div class="abs brand"><span class="dot"></span><span class="name">Pebble Lantern Kids</span></div>
  <nav class="abs main-nav">
    <span>Home</span><span>Our products</span><span>About us</span><span>Distributors</span><span>Blog</span><span>Contact</span>
    <span style="display:flex;align-items:center;gap:3px">
      <svg width="18" height="16" viewBox="0 0 18 16"><path d="M1 2h3l2 8h9l2-6H5" fill="none" stroke="#222" stroke-width="1.6"/><circle cx="7" cy="13.5" r="1.5" fill="#222"/><circle cx="14" cy="13.5" r="1.5" fill="#222"/></svg>Items</span>
  </nav>
</header>

<section class="abs hero">
  <h1 class="abs hero-title">When children become the heroes of their own stories</h1>
</section>
<div class="abs hero-photo" role="img" aria-label="Photo of a smiling mother reading a book with her young daughter"></div>
<svg class="abs clouds" viewBox="0 0 1200 70" preserveAspectRatio="none" aria-hidden="true">
  <path d="M0 40 Q30 5 70 30 Q110 0 150 28 Q200 -2 240 30 Q290 0 330 26 Q380 -4 420 28 Q470 2 510 30 Q560 0 600 26 Q650 -2 690 30 Q740 2 780 28 Q830 -2 870 30 Q920 0 960 26 Q1010 -2 1050 30 Q1100 0 1140 28 Q1175 6 1200 30 L1200 70 L0 70Z" fill="#eaf7fd"/>
</svg>

<section class="abs intro">
  <div class="col vision"><h2 class="section-title">Our Vision</h2>
    <p>Is to make children the heroes of the adventure and live magical and unforgettable moments they can share with their family and friends.<br>Scenarios are adapted to every age, imagined and conceived in association with children, schools, speech therapists, psychologists and childhood experts.</p></div>
  <div class="abs divider"></div>
  <div class="col mission"><h2 class="section-title">Our Mission</h2>
    <p>Personalisation offers for children to have an opportunity to recognise themselves in the story, thus developing the <b>morale, self-esteem and confidence.</b> All our stories aim to <b>stimulate learning and enhance reading passion</b> from an early age and have been designed with high-quality original artwork with bright colours to fully engage a child's imagination. The stories are written in an <b>educational and informative</b> way, <b>whilst remaining fun, positive, and engaging.</b></p></div>
</section>

<section class="abs products">
  <h2 class="section-title">Our Products</h2>
  <div class="product-card" style="left:252px;background:linear-gradient(160deg,#6b8a3a,#c9b27a 50%,#4d7a2c)" role="img" aria-label="Photo of a girl sitting outdoors with a storybook">
    <span class="btn">Books Shop</span></div>
  <div class="product-card" style="left:491px;background:linear-gradient(160deg,#f3f3f3,#e0c4b0 50%,#2a2a2a)" role="img" aria-label="Photo of a child singing with headphones on">
    <span class="btn">Music Dvd Shop</span></div>
  <div class="product-card" style="left:727px;background:linear-gradient(160deg,#f1ede8,#d9b79c 50%,#a7b4c8)" role="img" aria-label="Photo of a girl lying on the floor holding a remote">
    <span class="btn">Cartoon Dvd Shop</span></div>
</section>

<section class="abs about">
  <div class="about-copy">
    <h2 class="section-title">About Us</h2>
    <p>Maren Olsway Tibbet is an Entrepreneur, Author, Children's Education Innovator, and Advocate of Positive Change whose unwavering sense of ingenuity, passion, and dedication have earned her the reputation as a visionary leader in the childhood education space.Since launching Pebble Lantern Kids in 2012, she has been on a mission to help children tap into their infinite potential through personalized storybooks that enable them to get the most out of learning in an engaging way. Every month, her company sells thousands of storybooks, with distributors across 24 different countries.</p>
    <span class="btn">Read more</span>
  </div>
  <div class="abs book-mock" role="img" aria-label="Mockup of an open personalised storybook"></div>
</section>

<section class="abs blogs">
  <h2 class="section-title">Blogs</h2>
  <div class="abs arrows">
    <svg width="18" height="18" viewBox="0 0 18 18"><circle cx="9" cy="9" r="8" fill="none" stroke="#0392cd"/><path d="M10.5 5.5 7 9l3.5 3.5" fill="none" stroke="#0392cd" stroke-width="1.4"/></svg>
    <svg width="18" height="18" viewBox="0 0 18 18"><circle cx="9" cy="9" r="8" fill="none" stroke="#0392cd"/><path d="M7.5 5.5 11 9l-3.5 3.5" fill="none" stroke="#0392cd" stroke-width="1.4"/></svg>
  </div>
  <div class="blog-card" style="left:253px"><div class="thumb" role="img" aria-label="Illustrated book spread with a Christmas sleigh scene" style="background:linear-gradient(90deg,#1d3b8f,#3a5fc4 50%,#dfe6f4)"></div><p>It is a long established fact that a reader will be distracted by the readable content</p></div>
  <div class="blog-card" style="left:490px"><div class="thumb" role="img" aria-label="Illustrated book spread with a dinosaur scene" style="background:linear-gradient(90deg,#7fb6c8,#9ac27a 50%,#f2eee4)"></div><p>It is a long established fact that a reader will be distracted by the readable content</p></div>
  <div class="blog-card" style="left:733px"><div class="thumb" role="img" aria-label="Illustrated book spread with a farm tractor scene" style="background:linear-gradient(90deg,#f4efe0,#c94a3a 50%,#8cc364)"></div><p>It is a long established fact that a reader will be distracted by the readable content</p></div>
</section>

<div class="abs video" role="img" aria-label="Video still of children reading a book">
  <svg class="abs" style="left:192px;top:97px" width="36" height="36" viewBox="0 0 36 36"><circle cx="18" cy="18" r="16" fill="none" stroke="#fff" stroke-width="1.5"/><path d="M14 11v14l11-7z" fill="none" stroke="#fff" stroke-width="1.5"/></svg>
</div>
<div class="story">
  <h2>Personalisation improves a child's learning ability and motivation</h2>
  <p><b style="color:#555">Pebble Lantern Kids</b> personalised books offers the possibility of sharing magical and unique moments which help the child become familiar with reading and inspire reading passion. Which is more special and magical than becoming the hero of your own story !</p>
  <span class="btn">Read more</span>
</div>

<div class="abs garden" role="img" aria-label="Illustration of two cartoon children reading among flowers and a butterfly"></div>

<footer class="abs contact">
  <div class="contact-info">
    <h2>Get Touch</h2>
    <p class="lead">There are many variations of passages of Lorem Ipsum available, but the majority have suffered alteration in some form, by injected humour, or randomised words which don't look even slightly believable. If you are going to use a passage of Lorem Ipsum, you need to be sure there isn't anything embarrassing hidden in the middle of text. All the Lorem Ipsum generators on the Internet</p>
    <div class="contact-line">
      <svg width="14" height="14" viewBox="0 0 14 14"><circle cx="7" cy="7" r="7" fill="#fff"/><rect x="3.5" y="4.5" width="7" height="5" fill="none" stroke="#3f9a35"/><path d="M3.5 4.5 7 7.5l3.5-3" fill="none" stroke="#3f9a35"/></svg>
      <span>hello@pebblelanternkids.co.uk</span></div>
    <div class="contact-line">
      <svg width="14" height="14" viewBox="0 0 14 14"><circle cx="7" cy="7" r="7" fill="#fff"/><path d="M7 11s-3-3-3-5a3 3 0 0 1 6 0c0 2-3 5-3 5z" fill="#3f9a35"/></svg>
      <span>Unit 14, Alder Row,<br>Fernbrook FB3 7QL</span></div>
    <div class="contact-line">
      <svg width="14" height="14" viewBox="0 0 14 14"><circle cx="7" cy="7" r="7" fill="#fff"/><path d="M4.5 3.5h2l.8 2-1 .8a5 5 0 0 0 2.4 2.4l.8-1 2 .8v2c-4 .5-7.5-3-7-7z" fill="#3f9a35"/></svg>
      <span>01632-960-418</span></div>
  </div>
  <div class="abs form-panel">
    <div class="field" style="top:16px;height:40px">Name</div>
    <div class="field" style="top:68px;height:40px">Email</div>
    <div class="field" style="top:122px;height:80px">Comment</div>
    <div class="submit">Submit</div>
  </div>
</footer>
<div class="abs copyright">© 2018 pebble lantern kids</div>

</body>
</html>
```